Thank You Card design for a federal credit union

I am looking to have a thank you card designed.
Specs:
Flat size of 9.5"x6.5" folds to final size of 4.75"x6.5", it will print full color on the front and back. Below, you will see their logo, which needs to print on the inside of the folded card. I also attached images of their current card. They would like to keep the blue color but are open to design on the front. This is a Federal Credit Union, so please make the design, modern and professional. Below is the text that needs to print below the logo on the inside of the card. The text and logo will print below the fold on the inside, leave the top portion (above the panel) white.
Inside text:
Our Members are the foundation of our Credit Union. We sincerely thank you for your loyalty, your business and the opportunity to serve you.
Target Market(s)
Clients of a federal credit union
Industry/Entity Type
Union
Requirements
Must have
- a simple, professional, and modern feel. "Thank You for your business" must be on the front section in some variation.
Should not have
- nothing flashy or too many colors. keep it simple

```html
<!DOCTYPE html>
<html lang="en">
<head>
<meta charset="utf-8">
<title>Thank You Card – Flat Layout</title>
<link href="https://fonts.googleapis.com/css2?family=Lobster+Two:ital,wght@1,400;1,700&family=Open+Sans:ital,wght@1,400&display=swap" rel="stylesheet">
<style>
  :root {
    --page-bg: #ececec;
    --navy: #191948;
    --navy-light: #1f1f58;
    --brand-blue: #2e49a0;
    --paper: #ffffff;
    --fold: #8a8a9a;
    --ink-light: #ffffff;
  }
  * { margin: 0; padding: 0; box-sizing: border-box; }
  html, body {
    width: 1200px; height: 1200px; overflow: hidden;
    background: var(--page-bg);
  }
  .canvas { position: relative; width: 1200px; height: 1200px; }
  .sheet {
    position: absolute; top: 205px; width: 540px; height: 789px;
  }
  .sheet--outside { left: 40px; }
  .sheet--inside { left: 620px; background: var(--paper); border: 1px solid #cfcfcf; }

  .outside-surface {
    position: absolute; inset: 0;
    background: linear-gradient(180deg, var(--navy-light) 0%, var(--navy) 100%);
  }
  .fold-line {
    position: absolute; left: 0; right: 0; top: 394px; height: 1px;
    background: var(--fold);
  }
  .front-intro, .front-headline, .front-closing {
    position: absolute; color: var(--ink-light);
    font-family: "Lobster Two", cursive; font-style: italic;
  }
  .front-intro { left: 36px; top: 496px; font-size: 28px; font-weight: 700; }
  .front-headline {
    left: 58px; top: 560px; font-size: 86px; font-weight: 700;
    transform: rotate(-7deg); transform-origin: left bottom; white-space: nowrap;
  }
  .front-closing { right: 42px; top: 656px; font-size: 28px; font-weight: 700; }

  .brand-block {
    position: absolute; left: 0; right: 0; top: 478px;
    text-align: center; color: var(--brand-blue);
  }
  .brand-name {
    display: inline-flex; align-items: center; gap: 10px;
    font-family: "Lobster Two", cursive; font-style: italic; font-weight: 700;
    font-size: 30px; line-height: 1.1;
  }
  .brand-mark { width: 22px; height: 22px; background: var(--brand-blue); }
  .brand-sub {
    display: block; font-family: "Lobster Two", cursive; font-style: italic; font-weight: 700;
    font-size: 20px; margin-top: 2px;
  }
  .brand-tagline {
    font-family: "Open Sans", sans-serif; font-style: italic; font-size: 14px; margin-top: 8px;
  }
  .inside-message {
    position: absolute; left: 40px; right: 40px; top: 642px;
    text-align: center; color: var(--brand-blue);
    font-family: "Lobster Two", cursive; font-style: italic; font-size: 17px; line-height: 22px;
  }
</style>
</head>
<body>
<main class="canvas">
  <section class="sheet sheet--outside">
    <div class="outside-surface" role="img" aria-label="Deep navy background with a subtle geometric cube line pattern"></div>
    <div class="fold-line"></div>
    <p class="front-intro">We would like to say</p>
    <h1 class="front-headline">Thank You</h1>
    <p class="front-closing">for your business</p>
  </section>

  <section class="sheet sheet--inside">
    <div class="fold-line"></div>
    <div class="brand-block">
      <div class="brand-name"><span class="brand-mark"></span>Harborline</div>
      <span class="brand-sub">Federal Credit Union</span>
      <p class="brand-tagline">People Over Profits</p>
    </div>
    <p class="inside-message">Our Members are the foundation of our Credit Union.<br>We sincerely thank you for your loyalty, your business and<br>the opportunity to serve you.</p>
  </section>
</main>
</body>
</html>
```